Is your Will up to date?

We need a flyer that invites people to ask themselves if their Will is up to date.
In addition it is a known fact that people do not adjust their Will as often as they should to reflect their current wishes and circumstances.
Also, a large number of people end up having their estate pay taxes
that could be avoided if correct planning is in place.
We are offering a free of charge service the carry out a check to make sure families have in place a Will that suits their needs and circumstances and that has taken into account the tax positions and impact fully with a view to having the estate as tax efficient as possible.
A Will service is also part of the family check up.

Below is the suggested text for the flyer

A Will is one of the most important documents that we should all have. Many people are aware that if they die without having made a Will, then intestate rules apply which means in simple terms, that family assets and cash could end up in the hands of the Treasury.

While many people have looked at and acted upon creating a Will, it is fair to say that for many, the terms and wishes of the Will are often outdated. It is easy to assume that amending a Will frequently is a complicated process which it need not be.

An individual or a family Will is most important in order to ensure that upon death, your estate is dealt with and distributed in accordance with your wishes. This is also to ensure that any family are looked after by those provisions. Not only may family changes and additions affect a family Will, but there are also life changing situations that can have an effect.

Additionally, consideration needs to be given regularly to the current tax position, with specific regard to Inheritance Tax and how estate values can be legitimately reduced resulting in less tax to pay.

At Hartwell & Company we have the advantage of our Chartered Accountancy practice background, as well as also being Independent Financial Advisers. We are therefore well placed to advise families on the creation or updating of their Will, and to give advice on how to minimise tax payments.

Even for individuals and families that have had no significant changes in circumstances for many years, very often the beneficiaries may need to be updated, and even the appointment of Executors and Trustees needs to be addressed because very often, these instructions are considerably out of date.

A Will and all of its complex implications should be reviewed every one or two years and it is an extremely simple process to do this with our assistance.

So far as minimising payments for tax there are a wide range of effective methods that help do this. As general examples, there can be gifts made to family or a partner, gifts to friends, charitable donations, the use of insurance products to help settle tax liability as well as looking at placing assets into Trust. We have a wealth of experience in setting up the different types of Trust that exist and can help you easily understand how they would work for you.

When looking at the preparation of a Will, there are hundreds of questions that could be considered appropriate. However, with our experience and knowledge, and bespoke software this process can be covered within an initial meeting of less than one hour. You will have the re-assurance of knowing that every aspect has been carefully considered in preparing a Will to your circumstances and wishes.

The initial meeting and any follow up meetings are completely free of all cost and charges, and can be held at either our offices, or at your home if preferred.

We can just as easily deal with the process over the telephone if more convenient. Thereafter, we will prepare a draft Will for you, and give you confirmation as to the charges. In most cases, an individual or family Will would not normally involve charges in excess of £100.

So far as mitigating possible Inheritance Tax liabilities on the estate, we also offer the benefit of an asset and investment review at no cost. The individual or family assets are carefully considered, along with your requirements of income and growth and any specific requests or wishes that you wish to build into any trust or other methods of your choosing.

At the initial meeting or conference call we discuss all of these implications and will prepare a report and recommendations for your consideration, again free of charge. If you decide to act upon any of the recommendations, then any fees can be discussed and agreed at that stage.

All in all, whether you require assistance in preparing or updating a Will, or receiving independent advice regarding your estate assets or investments, these functions are carried out by us at no initial costs or charges.

At every step of the way there are never hidden charges or fees that you will be asked to be paid. We have over 30 years of experience in these market places, and value the service we give our clients and the reputation we gain from it.

We consider the review of a Will should be carried out at a minimum of every two years and it is a very small financial budget to allow for, against having the satisfaction of knowing these important matters are reflecting your current views, circumstances and wishes.

The same can be said for any trust and investment matters and any estate advice given. We are extremely proud and confident of the service we provide, and if any of our clients decide they do not wish to act upon the advice given, then they at least have had the benefit of a thorough review together with a recommendation without obligations of any sort.

To discuss these matters further or to make arrangements for a meeting please call our offices or email to derek@hartwellco-mail.co.uk

Content will be uploaded with next 24 hours

I am updating the brief with the wording.
It needs to be spread over the front and back of the flyer in an easy to read non boring design

Our firm logo will be updated shorty plus our Institute logo
Please make the flyer as catchy and interesting as possible.
Its a relatively boring topic for most people so it has to be eye catching rather than reading a page in a book

We will increase the budget if we are presented with a design we really like

Please note slightly amended text uploaded today

Target Market(s)

middle to upper class residents

Industry/Entity Type

Investment

Requirements
Must have
• Web address
Easy to read and understand
To look and feel catchy and not like reading a book
Some catchy graphics about tax, money, families etc

Fields where I can easily insert text and other details

```html
<!DOCTYPE html>
<html lang="en">
<head>
<meta charset="utf-8">
<title>Is your Will up to date? – Hartwell &amp; Co. flyer</title>
<link rel="stylesheet" href="https://fonts.googleapis.com/css2?family=Cormorant+SC:wght@500;600&family=Crimson+Text:wght@400;600&display=swap">
<style>
  :root{
    --red:#e8202a;
    --ink:#1a1a1a;
    --paper:#ffffff;
    --frame:#c9c9c9;
    --steel-dark:#1b1b1b;
    --steel-mid:#6b6b6b;
    --steel-light:#b9b9b9;
    --leaf:#6f9a3c;
    --leaf-light:#bcd48a;
  }
  *{box-sizing:border-box;margin:0;padding:0}
  html,body{width:1200px;height:768px;overflow:hidden;background:var(--paper)}
  body{position:relative;font-family:"Crimson Text",Georgia,serif;color:var(--ink)}

  .page{position:absolute;top:10px;height:750px;overflow:hidden}
  .page--front{left:10px;width:580px}
  .page--back{left:609px;width:582px;border:1px solid var(--frame)}

  .photo{position:absolute;display:block}

  .headline{position:absolute;font-family:"Cormorant SC",Georgia,serif;font-weight:600;line-height:1}
  .headline span{display:block;height:58px;font-size:44px}
  .headline .first{font-size:50px}
  .headline .accent{display:inline-block;background:var(--red);color:var(--paper);padding:2px 6px 6px;margin-left:-6px}

  /* front */
  .front-hero{left:0;top:0;width:580px;height:619px;
    background:radial-gradient(ellipse at 65% 55%,var(--steel-light) 0%,var(--steel-mid) 35%,var(--steel-dark) 80%)}
  .page--front .headline{left:30px;top:60px;color:var(--paper)}
  .front-band{position:absolute;left:0;top:619px;width:580px;height:131px;background:var(--red)}
  .front-band .family{left:35px;top:12px;width:228px;height:106px;
    background:linear-gradient(160deg,var(--leaf-light),var(--leaf) 70%,#4d7a2a)}
  .brand{position:absolute;display:flex;align-items:center;gap:8px;font-family:"Crimson Text",Georgia,serif;font-weight:600;line-height:1.05}
  .brand-mark{width:26px;height:26px;flex:none}
  .front-band .brand{left:318px;top:36px;color:var(--paper);font-size:22px}
  .front-band .brand .brand-mark{background:var(--paper)}
  .brand small{display:block;font-size:13px;font-weight:600}
  .web{position:absolute;font-size:15px;color:var(--paper)}
  .front-band .web{left:375px;top:101px}

  /* back */
  .back-main{position:absolute;left:0;top:0;width:420px;height:690px}
  .page--back .headline{left:10px;top:12px;color:var(--ink)}
  .page--back .headline span{height:49px;font-size:39px}
  .page--back .headline .first{font-size:44px}
  .portrait{left:164px;top:17px;width:235px;height:271px;
    background:radial-gradient(ellipse at 45% 40%,#8a8a8a,#3d3d3d 55%,#111 100%)}
  .body-copy{position:absolute;left:10px;top:293px;width:405px;font-size:11.2px;line-height:14px;text-align:justify}
  .body-copy p{margin-bottom:14px}
  .body-copy .closing{font-family:"Cormorant SC",Georgia,serif;font-weight:600;font-size:13.5px;line-height:17px;margin-bottom:0}
  .contact-bar{position:absolute;left:0;top:689px;width:420px;height:32px;background:var(--red);color:var(--paper);font-size:16px;padding:6px 14px}
  .phone-line{position:absolute;left:0;top:721px;width:420px;height:29px;font-size:16px;padding:4px 14px}

  .side-column{position:absolute;left:420px;top:0;width:162px;height:750px;background:var(--red);color:var(--paper)}
  .side-intro,.side-cta{position:absolute;left:6px;width:150px;font-family:"Cormorant SC",Georgia,serif;font-weight:600;text-align:justify}
  .side-intro{top:6px;font-size:12.4px;line-height:16.6px}
  .side-cta{top:555px;font-size:9.6px;line-height:12.3px}
  .institute-badge{position:absolute;left:36px;top:325px;width:90px;height:48px;background:var(--paper)}
  .institute-badge i{position:absolute;left:6px;top:8px;width:24px;height:32px;background:var(--red)}
  .side-column .family{left:0;top:400px;width:162px;height:115px;
    background:linear-gradient(160deg,var(--leaf-light),var(--leaf) 70%,#4d7a2a)}
  .side-footer{position:absolute;left:0;top:670px;width:162px;height:80px;background:var(--paper)}
  .side-footer .brand{left:12px;top:13px;color:var(--red);font-size:15px}
  .side-footer .brand small{font-size:9.5px}
  .side-footer .brand .brand-mark{width:20px;height:20px;background:var(--red)}
  .side-footer .web{left:0;width:162px;text-align:center;top:53px;color:var(--ink);font-size:13.5px}
</style>
</head>
<body>

<section class="page page--front">
  <div class="photo front-hero" role="img" aria-label="Close-up of a silver fountain pen nib touching a sparkling dark surface"></div>
  <h1 class="headline">
    <span class="first">Is</span>
    <span>your</span>
    <span><b class="accent">will</b></span>
    <span>up</span>
    <span>to</span>
    <span>date?</span>
  </h1>
  <div class="front-band">
    <div class="photo family" role="img" aria-label="Smiling three-generation family sitting together on grass"></div>
    <div class="brand"><i class="brand-mark"></i><div>Hartwell &amp; Co.<small>Chartered Accountants</small></div></div>
    <div class="web">www.hartwellco.co.uk</div>
  </div>
</section>

<section class="page page--back">
  <div class="back-main">
    <h2 class="headline">
      <span class="first">Is</span>
      <span>your</span>
      <span><b class="accent">will</b></span>
      <span>up</span>
      <span>to</span>
      <span>date?</span>
    </h2>
    <div class="photo portrait" role="img" aria-label="Black and white portrait of a thoughtful elderly man"></div>
    <div class="body-copy">
      <p>A Will is one of the most important documents that we should all have. Many people are aware that if they die without a Will being in existence, then intestate rules apply which means in simple terms, that family assets and cash could end up in the hands of the Treasury.</p>
      <p>While many people have looked and acted upon creating a Will, it is fair to say that for the majority, the terms and wishes of the Will are often outdated. It is easy to assume that amending a Will frequently is a complicated process which it need not be.</p>
      <p>An individual or a family Will is most important in order to ensure that your estate is dealt with and distributed in accordance with your wishes upon death. This is also to ensure that any family are looked after by those provisions. Not only may family changes and additions affect a family Will, but there are also life changing situations that can have an effect.</p>
      <p>Additionally, consideration needs to be given on a regular basis to the current tax position, with specific regards to Inheritance Tax and how estate values can be legitimately reduced resulting in less tax to pay.</p>
      <p>We have a wealth of experience in setting up of the different types of Trust that exists and help you easily understand how they work for you.</p>
      <p class="closing">A Will and all of its complex implications should be reviewed every one or two years and it is an extremely simple process to do this with our assistance. We help you to answer the hundreds of questions that you could consider regarding your Will.</p>
    </div>
    <div class="contact-bar">Please contact: derek@hartwellco-mail.co.uk</div>
    <div class="phone-line">Call us on 01632 960418</div>
  </div>

  <aside class="side-column">
    <p class="side-intro">At Hartwell &amp; Company we have the advantage of our Chartered Accountancy practice background, as well as also being Independent Financial Advisers. We are therefore well placed to advise families on the creation or updating of their Will, and to give advice on how to minimise tax payments. We have over 30 years of experience in these market places, and value the service we give our clients and the reputation we gain from it.</p>
    <div class="institute-badge" role="img" aria-label="Professional institute membership badge"><i></i></div>
    <div class="photo family" role="img" aria-label="Happy family of grandparents, parents and children outdoors"></div>
    <p class="side-cta">To make an appointment to discuss these matters either at our offices or at your home if preferred please either email to derek@hartwellco-mail.co.uk or telephone our office for a suitably convenient appointment time and date.</p>
    <div class="side-footer">
      <div class="brand"><i class="brand-mark"></i><div>Hartwell &amp; Co.<small>Chartered Accountants</small></div></div>
      <div class="web">www.hartwellco.co.uk</div>
    </div>
  </aside>
</section>

</body>
</html>
```